Design a Website Mockup for CampusLedger.org

Campusledger.org is NOT a public website, it is a web application which is used by universities. If you go to the website, you will see a basic mock-up of the application.

Your job is to take the basic layout and improve the design, layout and colors. The preferred color scheme would be based in blue.

Remember that this will be used by teachers and students, and the design should reflect good user interface design.

The basic elements required:

1. Logo to incorporate in the header.
2. Login link in upper right hand corner of Header.
3. Top Level Menu.
4. Second level menu (Page Level)
5. List students.
6. Add/Edit students.
7. Login Page.
8. Site Footer

Logo must be exported as PNG with transparent background.
All Photoshop files must be included.

```html
<!DOCTYPE html>
<html lang="en">
<head>
<meta charset="utf-8">
<title>CampusLedger – Student List</title>
<link rel="stylesheet" href="https://fonts.googleapis.com/css2?family=Open+Sans:wght@400;600&family=Arimo:wght@400&display=swap">
<style>
  :root {
    --sky-top: #5db9ee;
    --sky-bottom: #2f93d4;
    --nav-top: #6a6a6a;
    --nav-bottom: #3e3e3e;
    --nav-edge: #2c2c2c;
    --accent: #41a9e4;
    --link: #2a8fd2;
    --tab-idle: #b3b3b3;
    --tab-active: #eeeeee;
    --table-head: #e6e6e6;
    --row-line: #e3e3e3;
    --table-edge: #d6d6d6;
    --text-dark: #333333;
    --footer-top: #6d6d6d;
    --footer-bottom: #4a4a4a;
    --white: #ffffff;
  }
  * { box-sizing: border-box; margin: 0; padding: 0; }
  html, body { width: 1200px; height: 900px; overflow: hidden; background: var(--white); }
  body { position: relative; font-family: "Arimo", Arial, sans-serif; color: var(--text-dark); }

  .site-header {
    position: absolute; left: 0; top: 0; width: 1200px; height: 140px;
    background: linear-gradient(var(--sky-top), var(--sky-bottom));
  }
  .brand {
    position: absolute; left: 46px; top: 36px;
    font-family: "Open Sans", Arial, sans-serif; font-weight: 400;
    font-size: 42px; letter-spacing: 1px; color: var(--white);
  }
  .utility-links {
    position: absolute; right: 33px; top: 11px;
    font-family: "Open Sans", Arial, sans-serif; font-size: 16px; color: var(--white);
    display: flex; gap: 8px;
  }
  .utility-links a { color: var(--white); text-decoration: none; }
  .utility-links .sep { opacity: .7; }

  .main-nav {
    position: absolute; left: 171px; top: 123px; width: 860px; height: 50px;
    background: linear-gradient(var(--nav-top), var(--nav-bottom));
    border: 1px solid var(--nav-edge);
    font-family: "Open Sans", Arial, sans-serif; font-weight: 600; font-size: 19px; color: var(--white);
  }
  .main-nav .item { position: absolute; top: 12px; transform: translateX(-50%); white-space: nowrap; }
  .main-nav .item.current {
    top: 9px; padding: 2px 14px; background: var(--accent);
  }
  .main-nav .sep { position: absolute; top: 18px; width: 1px; height: 14px; background: #cfcfcf; }

  .page-tabs { position: absolute; left: 80px; top: 207px; height: 38px; }
  .page-tabs .tab {
    position: absolute; top: 0; height: 38px; width: 149px;
    border-radius: 4px 4px 0 0; background: var(--tab-idle);
    font-family: "Open Sans", Arial, sans-serif; font-size: 18px; color: var(--white);
    text-align: center; line-height: 38px;
  }
  .page-tabs .tab.active { background: var(--tab-active); color: var(--text-dark); }

  .student-table {
    position: absolute; left: 80px; top: 245px; width: 1040px;
    border-collapse: collapse; table-layout: fixed;
    border: 1px solid var(--table-edge); border-top: none;
  }
  .student-table th {
    height: 35px; background: var(--table-head);
    font-family: "Open Sans", Arial, sans-serif; font-weight: 400; font-size: 17px;
    color: var(--accent); text-align: center;
  }
  .student-table th.col-name { text-align: left; padding-left: 56px; }
  .student-table td {
    height: 35px; font-size: 14px; text-align: center;
    border-bottom: 1px solid var(--row-line);
  }
  .student-table td.col-name { text-align: left; padding-left: 36px; color: var(--link); }
  .student-table td.col-action svg { display: block; margin: 0 auto; }

  .site-footer {
    position: absolute; left: 0; top: 800px; width: 1200px; height: 100px;
    background: linear-gradient(var(--footer-top), var(--footer-bottom));
    color: var(--white); font-size: 14px;
  }
  .footer-links { position: absolute; left: 77px; top: 30px; display: flex; gap: 8px; }
  .footer-links .sep { opacity: .7; }
  .footer-tagline { position: absolute; left: 77px; top: 56px; }
  .footer-copyright { position: absolute; left: 905px; top: 31px; }
  .footer-release {
    position: absolute; left: 906px; top: 57px; padding-bottom: 2px;
    border-bottom: 1px solid var(--white);
  }
</style>
</head>
<body>
<svg width="0" height="0" style="position:absolute">
  <symbol id="icon-trash" viewBox="0 0 20 20">
    <g fill="none" stroke="#4aa7e0" stroke-width="1.5">
      <path d="M7 3h6M3 5h14"/>
      <path d="M5 5l1 13h8l1-13"/>
      <path d="M8.5 8v7M11.5 8v7"/>
    </g>
  </symbol>
</svg>

<header class="site-header">
  <div class="brand">CampusLedger</div>
  <nav class="utility-links">
    <a href="#">Login</a><span class="sep">|</span>
    <a href="#">Help</a><span class="sep">|</span>
    <a href="#">Reset Data</a>
  </nav>
</header>

<nav class="main-nav">
  <span class="item" style="left:73px">Home</span>
  <span class="sep" style="left:137px"></span>
  <span class="item" style="left:206px">About</span>
  <span class="sep" style="left:270px"></span>
  <span class="item" style="left:389px">Campusledger</span>
  <span class="sep" style="left:466px"></span>
  <span class="item current" style="left:560px">Students</span>
  <span class="sep" style="left:641px"></span>
  <span class="item" style="left:742px">Administration</span>
</nav>

<div class="page-tabs">
  <div class="tab active" style="left:0">Student List</div>
  <div class="tab" style="left:160px">Add New</div>
  <div class="tab" style="left:323px">Edit</div>
  <div class="tab" style="left:484px">View</div>
</div>

<table class="student-table">
  <colgroup>
    <col style="width:210px"><col style="width:190px"><col style="width:208px">
    <col style="width:206px"><col style="width:148px"><col style="width:78px">
  </colgroup>
  <thead>
    <tr><th class="col-name">NAME</th><th>GENDER</th><th>COUNTRY</th><th>SUBJECTS</th><th>STATUS</th><th></th></tr>
  </thead>
  <tbody>
    <tr><td class="col-name">Rafiq Noor</td><td>Male</td><td>Bangladesh</td><td>10</td><td>Studying</td><td class="col-action"><svg width="20" height="20"><use href="#icon-trash"/></svg></td></tr>
    <tr><td class="col-name">Tanvir Karim</td><td>Male</td><td>Bangladesh</td><td>12</td><td>Cleared</td><td class="col-action"><svg width="20" height="20"><use href="#icon-trash"/></svg></td></tr>
    <tr><td class="col-name">Nadia Rahman</td><td>Female</td><td>USA</td><td>2</td><td>Studying</td><td class="col-action"><svg width="20" height="20"><use href="#icon-trash"/></svg></td></tr>
    <tr><td class="col-name">Farhana Siddiq</td><td>Female</td><td>USA</td><td>15</td><td>Cleared</td><td class="col-action"><svg width="20" height="20"><use href="#icon-trash"/></svg></td></tr>
    <tr><td class="col-name">RupaDatta</td><td>Female</td><td>USA</td><td>14</td><td>Studying</td><td class="col-action"><svg width="20" height="20"><use href="#icon-trash"/></svg></td></tr>
    <tr><td class="col-name">Kamrul Hasan</td><td>Male</td><td>UK</td><td>10</td><td>Cleared</td><td class="col-action"><svg width="20" height="20"><use href="#icon-trash"/></svg></td></tr>
    <tr><td class="col-name">Rafiq Noor</td><td>Male</td><td>UK</td><td>10</td><td>Studying</td><td class="col-action"><svg width="20" height="20"><use href="#icon-trash"/></svg></td></tr>
    <tr><td class="col-name">Tanvir Karim</td><td>Female</td><td>UK</td><td>12</td><td>Cleared</td><td class="col-action"><svg width="20" height="20"><use href="#icon-trash"/></svg></td></tr>
    <tr><td class="col-name">Nadia Rahman</td><td>Female</td><td>UK</td><td>2</td><td>Studying</td><td class="col-action"><svg width="20" height="20"><use href="#icon-trash"/></svg></td></tr>
    <tr><td class="col-name">Farhana Siddiq</td><td>Female</td><td>UK</td><td>15</td><td>Cleared</td><td class="col-action"><svg width="20" height="20"><use href="#icon-trash"/></svg></td></tr>
    <tr><td class="col-name">RupaDatta</td><td>Female</td><td>UK</td><td>14</td><td>Studying</td><td class="col-action"><svg width="20" height="20"><use href="#icon-trash"/></svg></td></tr>
    <tr><td class="col-name">Kamrul Hasan</td><td>Female</td><td>UK</td><td>10</td><td>Cleared</td><td class="col-action"><svg width="20" height="20"><use href="#icon-trash"/></svg></td></tr>
    <tr><td class="col-name">Tanvir Karim</td><td>Male</td><td>UK</td><td>10</td><td>Cleared</td><td class="col-action"><svg width="20" height="20"><use href="#icon-trash"/></svg></td></tr>
  </tbody>
</table>

<footer class="site-footer">
  <div class="footer-links">
    <span>Contact us</span><span class="sep">|</span>
    <span>About us</span><span class="sep">|</span>
    <span>Help</span><span class="sep">|</span>
    <span>FAQ</span>
  </div>
  <div class="footer-tagline">Campusledger - Education in Real Time</div>
  <div class="footer-copyright">Copyright © 2014 Campusledger, Inc</div>
  <div class="footer-release">Product Release: v7.0</div>
</footer>
</body>
</html>
```